E-learning Information & Community Website Needs a Makeover

I'm looking for a design makeover for my website "Vetrola.club". Vetrola's aim is to connect people to online learning through forums, information, guides & independent reviews. The site was launched in September 2014 using a forum software (Xenforo), but now needs a more polished and sophisticated look which communicates expertise and professionalism. I would like to see designs that use the current "Vetrola" blue (#0070c0). To visit the current website, go to http://www.vetrola.club/

Target Market(s)

People wishing to study online

Industry/Entity Type

Club

Number of Pages Required

4 page

Font styles to use
Sans Serif

Requirements
Must have
• A simple, clear and sophisticated lading page with links to the site's key features: discussion forums, Useful resources, Reviews, News etc, Articles. (See layout idea file attached)
• The main pages are the Landing Page, Discussion Forums, Resources & Reviews
• I would like to see designs that use the current "Vetrola" blue (#0070c0).
Nice to have
• Something uncluttered and easy to understand. The design should convey expertise in the field of online learning, giving users a sense of trust in the site's offerings.
• To give an idea of the sort of thing I'm after, take a look at brantivo.com website (screenshot attached)

```html
<!DOCTYPE html>
<html lang="en">
<head>
<meta charset="utf-8">
<title>Vetrola – Connecting People to Online Learning</title>
<link rel="stylesheet" href="https://fonts.googleapis.com/css2?family=Open+Sans:wght@400;600;700&family=Oswald:wght@300;400&display=swap">
<style>
  :root {
    --brand: #0070c0;
    --brand-dark: #005fa6;
    --ink: #1b1b1b;
    --muted: #777;
    --line: #e3e3e3;
    --panel: #f2f2f2;
    --red: #cc5656;
    --red-soft: #d06060;
    --sky: #72b0d8;
    --mint: #6cc3ac;
    --white: #fff;
  }
  * { box-sizing: border-box; margin: 0; padding: 0; }
  html, body { width: 735px; height: 1200px; overflow: hidden; }
  body { font-family: "Open Sans", Arial, sans-serif; color: var(--ink); background: var(--white); position: relative; }
  a { color: inherit; text-decoration: none; }

  /* Header */
  .site-header { position: absolute; top: 0; left: 0; width: 735px; height: 36px; background: var(--brand); color: var(--white); }
  .brand { position: absolute; left: 45px; top: 5px; }
  .brand-name { font-size: 13px; line-height: 14px; font-weight: 400; }
  .brand-tagline { font-size: 5.5px; line-height: 7px; }
  .main-nav { position: absolute; left: 243px; top: 13px; display: flex; gap: 21px; font-size: 8.5px; text-transform: uppercase; }
  .auth { position: absolute; right: 45px; top: 10px; display: flex; gap: 7px; }
  .auth a { border: 1px solid var(--white); border-radius: 2px; font-size: 8px; padding: 2px 5px; line-height: 10px; text-transform: uppercase; }

  /* Hero */
  .hero { position: absolute; top: 36px; left: 0; width: 735px; height: 280px; background: linear-gradient(90deg, #f1f1f1 0%, #f7f7f7 45%, #ececec 100%); overflow: hidden; }
  .hero-photo { position: absolute; left: 340px; top: 0; width: 395px; height: 280px;
    background: radial-gradient(ellipse at 62% 42%, #d9cfc7 0%, #c8c2be 22%, transparent 48%), linear-gradient(90deg, rgba(240,240,240,0) 0%, #e4e1de 25%, #d7d3cf 100%); }
  .hero-title { position: absolute; left: 45px; top: 80px; font-family: "Oswald", "Arial Narrow", sans-serif; font-weight: 400; font-size: 21px; line-height: 22px; color: #222; text-transform: uppercase; letter-spacing: -0.2px; }
  .hero-title em { font-style: normal; color: var(--brand); }
  .btn-signup { position: absolute; left: 45px; top: 145px; width: 103px; height: 25px; background: var(--brand); color: var(--white); font-size: 9px; line-height: 25px; text-align: center; text-transform: uppercase; border-radius: 2px; }
  .slide-label { position: absolute; left: 186px; top: 243px; font-size: 10.5px; font-weight: 700; letter-spacing: .3px; }
  .slide-dots { position: absolute; left: 45px; top: 257px; display: flex; gap: 3px; }
  .slide-dots span { width: 5px; height: 5px; border-radius: 50%; background: #c9c9c9; }
  .slide-dots span.is-active { background: #8aa6c0; }

  /* Feature tiles */
  .features { position: absolute; top: 334px; left: 128px; width: 480px; display: grid; grid-template-columns: repeat(3, 148px); column-gap: 17px; row-gap: 18px; }
  .tile { height: 129px; border: 2px solid #e8e8e8; background: var(--white); text-align: center; padding-top: 11px; }
  .tile-title { font-family: "Oswald", "Arial Narrow", sans-serif; font-weight: 300; font-size: 12.5px; text-transform: uppercase; line-height: 14px; }
  .tile-icon { display: block; margin: 13px auto 0; width: 72px; height: 72px; }
  .t-red { color: var(--red); } .t-sky { color: var(--sky); } .t-mint { color: var(--mint); }

  .divider { position: absolute; top: 636px; left: 45px; width: 598px; height: 1px; background: var(--line); }
  .more-toggle { position: absolute; top: 627px; left: 358px; width: 18px; height: 18px; }

  /* Community */
  .community { position: absolute; top: 680px; left: 0; width: 735px; height: 461px; background: var(--panel); }
  .section-title { position: absolute; top: 30px; width: 735px; text-align: center; font-family: "Oswald", "Arial Narrow", sans-serif; font-size: 13px; color: var(--brand); text-transform: uppercase; }
  .threads { position: absolute; top: 62px; left: 37px; width: 661px; background: var(--white); }
  .threads-head { height: 37px; background: var(--brand); color: var(--white); font-size: 8.5px; font-weight: 600; text-transform: uppercase; position: relative; }
  .threads-head span { position: absolute; top: 13px; }
  .thread { position: relative; height: 55px; border-bottom: 1px solid #ececec; }
  .thread:last-child { border-bottom: 0; }
  .avatar { position: absolute; left: 8px; top: 11px; width: 33px; height: 33px; background: var(--brand); color: var(--white); font-size: 6.5px; text-align: center; line-height: 33px; }
  .tag { position: absolute; left: 52px; top: 10px; width: 38px; height: 10px; border-radius: 2px; color: var(--white); font-size: 5px; font-weight: 700; text-align: center; line-height: 10px; text-transform: uppercase; }
  .tag-advise { background: var(--brand); } .tag-review { background: var(--mint); } .tag-article { background: var(--red-soft); }
  .thread-title { position: absolute; left: 52px; top: 25px; font-size: 9.5px; font-weight: 600; }
  .thread-meta { position: absolute; left: 52px; top: 39px; font-size: 7px; color: var(--muted); }
  .stat-label { position: absolute; left: 449px; color: var(--muted); }
  .stat-label.replies { top: 15px; font-size: 9px; }
  .stat-label.views { top: 30px; font-size: 7px; }
  .stat-value { position: absolute; color: #333; }
  .stat-value.replies { left: 505px; top: 15px; font-size: 9px; }
  .stat-value.views { left: 503px; top: 30px; font-size: 7px; }
  .last-user { position: absolute; left: 560px; top: 15px; font-size: 9px; font-weight: 700; }
  .last-date { position: absolute; left: 560px; top: 28px; font-size: 7px; color: var(--muted); }

  /* Footer */
  .site-footer { position: absolute; top: 1141px; left: 0; width: 735px; height: 59px; background: var(--brand); color: var(--white); }
  .footer-nav { position: absolute; left: 50px; top: 20px; font-size: 7.5px; text-transform: uppercase; }
  .footer-nav span { margin: 0 4px; }
  .copyright { position: absolute; left: 50px; top: 32px; font-size: 7.5px; text-transform: uppercase; }
  .social { position: absolute; right: 50px; top: 20px; display: flex; gap: 3px; }
  .social span { width: 19px; height: 19px; border: 1.5px solid var(--white); border-radius: 50%; }
</style>
</head>
<body>

<header class="site-header">
  <div class="brand">
    <div class="brand-name">Vetrola</div>
    <div class="brand-tagline">Connecting People to Online Learning</div>
  </div>
  <nav class="main-nav">
    <a href="#">Home</a><a href="#">Discussion Forums</a><a href="#">Usefu Resources</a><a href="#">Reviews</a><a href="#">News</a>
  </nav>
  <div class="auth"><a href="#">Login</a><a href="#">Register</a></div>
</header>

<section class="hero">
  <div class="hero-photo" role="img" aria-label="Photo of a smiling student in a striped top working on a laptop in a bright room with bookshelves"></div>
  <h1 class="hero-title">At the heartof connecting<br>people to <em>online learning</em></h1>
  <a class="btn-signup" href="#">Signup for free</a>
  <div class="slide-label">REVIEWS</div>
  <div class="slide-dots"><span></span><span class="is-active"></span><span></span><span></span><span></span></div>
</section>

<section class="features">
  <a class="tile" href="#">
    <div class="tile-title t-red">Getting Started</div>
    <svg class="tile-icon" viewBox="0 0 72 72"><circle cx="36" cy="36" r="36" fill="#cc5656"/><circle cx="36" cy="36" r="20" fill="none" stroke="#f3d9c9" stroke-width="5"/><path d="M31 26 L47 36 L31 46 Z" fill="#e8a44a"/></svg>
  </a>
  <a class="tile" href="#">
    <div class="tile-title t-sky">Discussions</div>
    <svg class="tile-icon" viewBox="0 0 72 72"><circle cx="36" cy="36" r="36" fill="#72b0d8"/><path d="M36 18 C24 18 17 25 17 34 C17 40 20 44 25 47 L22 55 L32 49 C33 49 35 50 36 50 C48 50 55 43 55 34 C55 25 48 18 36 18 Z" fill="#fff" stroke="#4d6f88" stroke-width="1.5"/><circle cx="29" cy="34" r="2" fill="#4d6f88"/><circle cx="36" cy="34" r="2" fill="#4d6f88"/><circle cx="43" cy="34" r="2" fill="#4d6f88"/></svg>
  </a>
  <a class="tile" href="#">
    <div class="tile-title t-red">Reviews</div>
    <svg class="tile-icon" viewBox="0 0 72 72"><circle cx="36" cy="36" r="36" fill="#cc5656"/><path d="M36 14 L42.5 28 L57 29.5 L46 39.5 L49.5 54 L36 46.5 L22.5 54 L26 39.5 L15 29.5 L29.5 28 Z" fill="#f4c55a" stroke="#e0a43b" stroke-width="1.5" stroke-linejoin="round"/></svg>
  </a>
  <a class="tile" href="#">
    <div class="tile-title t-mint">Tips &amp; Guidelines</div>
    <svg class="tile-icon" viewBox="0 0 72 72"><circle cx="36" cy="36" r="36" fill="#6cc3ac"/><path d="M14 31 H22 V42 H14 Z" fill="#cc5656"/><path d="M22 31 L46 20 V53 L22 42 Z" fill="#eee"/><rect x="46" y="19" width="5" height="35" rx="2" fill="#cc5656"/><path d="M18 42 L22 42 L25 52 L20 52 Z" fill="#4d5a66"/></svg>
  </a>
  <a class="tile" href="#">
    <div class="tile-title t-red">News &amp; Articles</div>
    <svg class="tile-icon" viewBox="0 0 72 72"><circle cx="36" cy="36" r="36" fill="#cc5656"/><rect x="18" y="20" width="36" height="32" fill="#efe6d6"/><rect x="21" y="23" width="30" height="4" fill="#3b4a5a"/><rect x="21" y="30" width="13" height="11" fill="#6c8aa8"/><path d="M37 31h14M37 34h14M37 37h14M37 40h14M21 44h30M21 47h30" stroke="#6b6b6b" stroke-width="1.2"/></svg>
  </a>
  <a class="tile" href="#">
    <div class="tile-title t-sky">Newsletter</div>
    <svg class="tile-icon" viewBox="0 0 72 72"><circle cx="36" cy="36" r="36" fill="#72b0d8"/><rect x="15" y="24" width="42" height="26" rx="1.5" fill="#f2efe4"/><path d="M15 25 L36 40 L57 25" fill="none" stroke="#c9c3b2" stroke-width="1.5"/><path d="M15 50 L31 36 M57 50 L41 36" stroke="#d8d2c1" stroke-width="1.2"/></svg>
  </a>
</section>

<div class="divider"></div>
<svg class="more-toggle" viewBox="0 0 18 18"><circle cx="9" cy="9" r="8" fill="#fff" stroke="#555" stroke-width="1.5"/><path d="M5.5 7.5 L9 11 L12.5 7.5" fill="none" stroke="#555" stroke-width="1.5"/></svg>

<section class="community">
  <h2 class="section-title">Fromthe Community</h2>
  <div class="threads">
    <div class="threads-head">
      <span style="left:16px">Recent Threads</span>
      <span style="left:449px">Replies</span>
      <span style="left:504px">Views</span>
      <span style="left:559px">Last Message</span>
    </div>

    <div class="thread">
      <div class="avatar">Vetrola</div><div class="tag tag-advise">Advise</div>
      <div class="thread-title">Effective learning: On-demand vs scheduled courses</div>
      <div class="thread-meta">TomR, Yesterday at 9:44 AM, MOOC Advice</div>
      <div class="stat-label replies">Replies:</div><div class="stat-value replies">2</div>
      <div class="stat-label views">Views:</div><div class="stat-value views">20</div>
      <div class="last-user">Kiro</div><div class="last-date">Yesterday at 1:26 PM</div>
    </div>
    <div class="thread">
      <div class="avatar">Vetrola</div><div class="tag tag-review">Review</div>
      <div class="thread-title">Effective learning: On-demand vs scheduled courses</div>
      <div class="thread-meta">TomR, Yesterday at 9:44 AM, MOOC Advice</div>
      <div class="stat-label replies">Replies:</div><div class="stat-value replies">2</div>
      <div class="stat-label views">Views:</div><div class="stat-value views">20</div>
      <div class="last-user">Kiro</div><div class="last-date">Yesterday at 1:26 PM</div>
    </div>
    <div class="thread">
      <div class="avatar">Vetrola</div><div class="tag tag-article">Article</div>
      <div class="thread-title">Effective learning: On-demand vs scheduled courses</div>
      <div class="thread-meta">TomR, Yesterday at 9:44 AM, MOOC Advice</div>
      <div class="stat-label replies">Replies:</div><div class="stat-value replies">2</div>
      <div class="stat-label views">Views:</div><div class="stat-value views">20</div>
      <div class="last-user">Kiro</div><div class="last-date">Yesterday at 1:26 PM</div>
    </div>
    <div class="thread">
      <div class="avatar">Vetrola</div><div class="tag tag-advise">Advise</div>
      <div class="thread-title">Effective learning: On-demand vs scheduled courses</div>
      <div class="thread-meta">TomR, Yesterday at 9:44 AM, MOOC Advice</div>
      <div class="stat-label replies">Replies:</div><div class="stat-value replies">2</div>
      <div class="stat-label views">Views:</div><div class="stat-value views">20</div>
      <div class="last-user">Kiro</div><div class="last-date">Yesterday at 1:26 PM</div>
    </div>
    <div class="thread">
      <div class="avatar">Vetrola</div><div class="tag tag-advise">Advise</div>
      <div class="thread-title">Effective learning: On-demand vs scheduled courses</div>
      <div class="thread-meta">TomR, Yesterday at 9:44 AM, MOOC Advice</div>
      <div class="stat-label replies">Replies:</div><div class="stat-value replies">2</div>
      <div class="stat-label views">Views:</div><div class="stat-value views">20</div>
      <div class="last-user">Kiro</div><div class="last-date">Yesterday at 1:26 PM</div>
    </div>
    <div class="thread">
      <div class="avatar">Vetrola</div><div class="tag tag-advise">Advise</div>
      <div class="thread-title">Effective learning: On-demand vs scheduled courses</div>
      <div class="thread-meta">TomR, Yesterday at 9:44 AM, MOOC Advice</div>
      <div class="stat-label replies">Replies:</div><div class="stat-value replies">2</div>
      <div class="stat-label views">Views:</div><div class="stat-value views">20</div>
      <div class="last-user">Kiro</div><div class="last-date">Yesterday at 1:26 PM</div>
    </div>
  </div>
</section>

<footer class="site-footer">
  <nav class="footer-nav">Home<span>|</span>Discussion Forums<span>|</span>Usefu Resources<span>|</span>Reviews<span>|</span>News</nav>
  <div class="copyright">Copyright © 2015 Vetrola. All rights reserved.</div>
  <div class="social" aria-label="Social links"><span></span><span></span><span></span></div>
</footer>

</body>
</html>
```